Life and Personal development life coach needs card design

I need a card design that matches the style and design of my website. I'd like to stay in the same color scheme. Please check out my website for ideas. www.bretamoorvale.com
I have had previous designs for this. I am wondering if you have access to those for more ideas??

```html
<!DOCTYPE html>
<html lang="en">
<head>
<meta charset="utf-8">
<title>Breta Moorvale – Life Coach Business Card</title>
<link href="https://fonts.googleapis.com/css2?family=Alegreya:wght@400;700&display=swap" rel="stylesheet">
<style>
  :root {
    --page-bg: #e9eaee;
    --navy-deep: #0a0d24;
    --navy-mid: #171c44;
    --navy-glow: #232a5e;
    --ink-light: #f3f4f8;
    --ink-soft: #d9dcea;
    --photo-cream: #efe6cf;
    --photo-blue: #2c3a78;
    --photo-dark: #1a2150;
  }
  * { box-sizing: border-box; margin: 0; padding: 0; }
  html, body {
    width: 1200px; height: 926px; overflow: hidden;
    background: var(--page-bg);
    font-family: "Alegreya", Georgia, serif;
  }
  .canvas {
    width: 1200px; height: 926px;
    display: flex; flex-direction: column;
    align-items: center; justify-content: center; gap: 44px;
  }
  .card {
    width: 700px; height: 400px;
    position: relative; overflow: hidden;
    box-shadow: 0 10px 28px rgba(10, 13, 36, 0.25);
    color: var(--ink-light);
  }
  .card--front {
    background: radial-gradient(ellipse at 50% 40%, var(--navy-glow) 0%, var(--navy-mid) 45%, var(--navy-deep) 100%);
    display: flex; flex-direction: column; align-items: center; justify-content: center;
  }
  .front__title {
    font-size: 54px; font-weight: 400; letter-spacing: 0.16em;
  }
  .front__tagline {
    margin-top: 6px; font-size: 22px; letter-spacing: 0.14em; color: var(--ink-soft);
  }
  .card--back { display: flex; }
  .back__photo {
    width: 330px; height: 100%;
    background: linear-gradient(100deg, var(--photo-cream) 0%, var(--photo-cream) 18%, var(--photo-blue) 45%, var(--photo-dark) 100%);
  }
  .back__panel {
    flex: 1; position: relative; padding: 36px 32px;
    background: radial-gradient(ellipse at 30% 20%, var(--navy-glow) 0%, var(--navy-mid) 50%, var(--navy-deep) 100%);
  }
  .back__name { font-size: 30px; font-weight: 400; line-height: 1.1; }
  .back__name strong { font-weight: 700; }
  .back__role { font-size: 17px; letter-spacing: 0.14em; color: var(--ink-soft); margin-top: 2px; }
  .back__contacts {
    position: absolute; left: 32px; bottom: 34px;
    list-style: none; font-size: 19px; line-height: 1.45; color: var(--ink-light);
  }
</style>
</head>
<body>
<main class="canvas">
  <section class="card card--front">
    <h1 class="front__title">LIFE COACH</h1>
    <p class="front__tagline">Discover what is possible today!</p>
  </section>

  <section class="card card--back">
    <div class="back__photo" role="img" aria-label="Portrait photo of the coach wearing a dark hat and blue cardigan"></div>
    <div class="back__panel">
      <h2 class="back__name">Breta <strong>Moorvale</strong></h2>
      <p class="back__role">LIFE COACH</p>
      <ul class="back__contacts">
        <li>P: 619-555-0148,</li>
        <li>W: www.bretamoorvale.com</li>
        <li>E: breta@bretamoorvale.com</li>
      </ul>
    </div>
  </section>
</main>
</body>
</html>
```